Vellart

I already have a website created through Makrive.com - https://vellart.co.nz.

Its an accounting services business, can get ideas from wexo.co.nz, fyn.co.nz, hul.co.nz

I would like to have this recreated using coding. I need the following features and functionalities incorporated:

- Live Chat feature
- Moving Carousel feature for Reviews
- Advanced SEO support (Google Analytics)

Industry/Entity Type

accounting

Coding

Coded - Design and coding required

Number of Pages Required

5+ page

```html
<!DOCTYPE html>
<html lang="en">
<head>
<meta charset="utf-8">
<title>Vellart — Accounting Services</title>
<meta name="viewport" content="width=1200">
<link href="https://fonts.googleapis.com/css2?family=Poppins:ital,wght@0,300;0,400;0,500;0,600;0,700;1,400;1,500&display=swap" rel="stylesheet">
<style>
:root{
  --slate:#3d4a49;
  --slate-deep:#334040;
  --mint:#a8d8cb;
  --mint-soft:#cbe9e1;
  --teal:#5db4a0;
  --ink:#2b2f30;
  --body:#4a4f50;
  --white:#ffffff;
  --line:#d9dedd;
  --star:#f1b81f;
}
*{box-sizing:border-box;margin:0;padding:0}
html,body{width:1200px;height:5204px;overflow:hidden}
body{font-family:"Poppins",sans-serif;color:var(--ink);background:var(--white);position:relative}
.pill{position:absolute;display:flex;align-items:center;justify-content:center;gap:10px;border-radius:30px;font-weight:500;letter-spacing:.5px}
.pill svg{width:24px;height:24px}
.pill-dark{background:var(--slate);color:var(--white)}
.pill-outline{border:2px solid var(--mint);color:var(--white)}
/* header */
.site-header{position:absolute;left:0;top:0;width:1200px;height:162px;background:var(--slate)}
.nav-link{position:absolute;top:62px;font-size:15px;color:var(--white);letter-spacing:.5px}
.nav-link.active{color:var(--mint);border-bottom:2px solid var(--mint);padding-bottom:3px}
.brand{position:absolute;display:flex;align-items:center;justify-content:center;gap:12px;left:450px;width:300px}
.brand-mark{width:18px;height:18px;border-radius:50%;background:var(--mint)}
.brand-name{font-weight:600;color:var(--mint);letter-spacing:6px}
.header-brand{top:58px}
.header-brand .brand-name{font-size:30px}
.chat-btn{left:1002px;top:57px;width:133px;height:40px;background:var(--mint);color:var(--slate);font-size:14px}
/* hero */
.hero-photo{position:absolute;left:0;top:162px;width:1200px;height:802px;background:linear-gradient(120deg,#2a3c52 0%,#4f5d6a 30%,#8f8a82 55%,#5d544c 80%,#3a3431 100%)}
.hero-overlay{position:absolute;left:0;top:162px;width:1200px;height:802px}
.hero-title{position:absolute;right:65px;top:298px;text-align:right;color:var(--white);font-size:50px;line-height:61px;font-weight:400}
.hero-btn{left:927px;top:570px;width:208px;height:50px;font-size:18px}
/* features */
.feature{position:absolute;top:1010px;width:330px;height:206px;background:var(--mint);border-radius:14px;text-align:center;color:var(--slate)}
.feature svg{position:absolute;left:50%;transform:translateX(-50%);top:28px}
.feature p{position:absolute;left:0;right:0;top:112px;font-size:27px;line-height:32px}
/* about */
.about-photo{position:absolute;left:65px;top:1327px;width:456px;height:424px;border-radius:50%;background:radial-gradient(circle at 45% 45%,#e8eef3 0%,#b9c9d6 45%,#5f7e98 80%,#3c5670 100%)}
.section-title{position:absolute;font-size:47px;font-weight:600;color:var(--ink);line-height:1}
.kicker{position:absolute;font-size:17px;color:var(--ink);display:flex;align-items:center;gap:6px}
.kicker .rule{display:inline-block;height:1px;background:var(--ink);width:70px}
.kicker .dot{display:inline-block;width:11px;height:11px;border:1.5px solid var(--ink);border-radius:50%;position:relative}
.kicker .dot::after{content:"";position:absolute;left:2.5px;top:2.5px;width:3px;height:3px;background:var(--ink);border-radius:50%}
.about-copy{position:absolute;left:618px;width:522px;font-size:12.8px;line-height:24px;color:var(--body)}
.about-btn{left:618px;top:1693px;width:178px;height:48px;font-size:15px}
/* banner */
.banner-photo{position:absolute;left:0;top:1919px;width:1200px;height:475px;background:linear-gradient(100deg,#8fa9b4 0%,#c9c1b4 30%,#9c7656 50%,#c7ccce 70%,#3f5263 100%)}
.banner-strip{position:absolute;left:0;top:1919px;width:14px;height:475px;background:var(--mint)}
.banner-ring{position:absolute;left:705px;top:1930px;width:450px;height:450px;border-radius:50%;border:34px solid rgba(168,216,203,.45)}
.banner-circle{position:absolute;left:728px;top:1955px;width:394px;height:394px;border-radius:50%;background:rgba(235,238,238,.94)}
.banner-text{position:absolute;left:760px;width:330px;top:2060px;text-align:center;font-size:26px;line-height:34px;font-weight:600;color:var(--slate)}
.banner-btn{left:838px;top:2266px;width:176px;height:47px;font-size:16px}
/* services */
.centered{left:0;width:1200px;justify-content:center;text-align:center}
.services-intro{position:absolute;left:160px;width:880px;top:2628px;text-align:center;font-size:16px;line-height:27px;color:var(--ink)}
.service{position:absolute;width:328px;height:280px;background:var(--white);border-radius:10px;box-shadow:0 3px 12px rgba(0,0,0,.18)}
.service.highlight{background:var(--mint);box-shadow:none}
.service-icon{position:absolute;left:24px;top:20px;width:96px;height:96px;border-radius:50%;background:var(--slate);border:3px solid var(--white);box-shadow:0 0 0 2px var(--slate)}
.service-icon svg{position:absolute;left:21px;top:21px}
.service h3{position:absolute;left:30px;right:24px;top:130px;font-size:21px;font-weight:500;line-height:25px;color:var(--ink)}
.service p{position:absolute;left:30px;right:30px;font-size:13.5px;line-height:24px;color:var(--body)}
.read-more{position:absolute;left:30px;top:244px;font-size:12px;font-weight:600;display:flex;align-items:center;gap:8px;color:var(--ink)}
.services-btn{left:485px;top:3398px;width:230px;height:48px;font-size:16px}
/* reviews */
.review{position:absolute;top:3733px;width:344px;height:188px;background:var(--slate);border-radius:4px;text-align:center;color:var(--white)}
.review::after{content:"";position:absolute;left:40px;bottom:-14px;border-left:12px solid transparent;border-right:12px solid transparent;border-top:14px solid var(--slate)}
.review .quote{position:absolute;left:0;right:0;top:6px;font-size:80px;line-height:80px;color:#7b8786;font-weight:700}
.review p{position:absolute;left:22px;right:22px;top:70px;font-size:13.3px;line-height:23px;font-style:italic;font-weight:500}
.review .stars{position:absolute;left:0;right:0;top:166px;font-size:12px;color:var(--star);letter-spacing:1px;line-height:14px}
.reviewer{position:absolute;top:3958px;display:flex;align-items:center;gap:14px}
.avatar{width:74px;height:74px;border-radius:50%;background:linear-gradient(160deg,#c9d2d6,#7f8b92)}
.reviewer b{display:block;font-size:16px;font-weight:600;color:var(--ink)}
.reviewer span{display:block;font-size:12px;color:var(--body);line-height:14px}
.arrow{position:absolute;top:3800px;width:44px;height:44px;border-radius:50%;display:flex;align-items:center;justify-content:center}
.dots{position:absolute;top:4064px;left:566px;display:flex;gap:8px}
.dots i{width:10px;height:10px;border-radius:50%;border:1.5px solid #8b9190}
.dots i.on{background:var(--slate);border-color:var(--slate)}
/* contact */
.contact-photo{position:absolute;left:77px;top:4181px;width:500px;height:526px;border-radius:50%;background:radial-gradient(circle at 50% 45%,#d8dde4 0%,#a88f82 40%,#6d5750 70%,#e9ecee 96%)}
.contact-lead{position:absolute;left:617px;top:4262px;font-size:14px;color:var(--ink)}
.field{position:absolute;border:1.5px solid var(--line);background:var(--white);font-size:12.5px;color:#9aa09f;padding:11px 18px}
.submit-btn{left:608px;top:4620px;width:206px;height:48px;font-size:19px}
/* footer */
.site-footer{position:absolute;left:0;top:4797px;width:1200px;height:407px;background:var(--slate);color:var(--white)}
.footer-head{position:absolute;font-size:18px;font-weight:500;letter-spacing:.5px}
.footer-head::after{content:"";position:absolute;left:0;top:34px;width:125px;height:2px;background:var(--mint)}
.quick-links{position:absolute;left:284px;top:122px;list-style:none;font-size:15px;line-height:27.5px}
.quick-links li::before{content:"";display:inline-block;width:9px;height:9px;border:1.5px solid var(--mint);border-radius:50%;margin-right:7px}
.footer-brand{top:140px}
.footer-brand .brand-name{font-size:29px}
.social{position:absolute;top:248px;left:538px;display:flex;gap:6px}
.social i{width:32px;height:32px;border-radius:50%;background:var(--white)}
.contact-item{position:absolute;left:760px;display:flex;gap:18px;align-items:center;font-size:14px;line-height:16px}
.contact-item .ico{width:26px;height:26px;border:1.5px solid #9aa5a4;border-radius:4px;display:flex;align-items:center;justify-content:center}
.footer-rule{position:absolute;left:66px;top:314px;width:1068px;height:1px;background:#8f9a99}
.copyright{position:absolute;left:0;width:1200px;top:345px;text-align:center;font-size:11px}
</style>
</head>
<body>

<header class="site-header">
  <a class="nav-link active" style="left:185px">HOME</a>
  <a class="nav-link" style="left:273px">SERVICES</a>
  <a class="nav-link" style="left:388px">ABOUT US</a>
  <div class="brand header-brand"><span class="brand-mark"></span><span class="brand-name">VELLART</span></div>
  <a class="nav-link" style="left:747px;top:70px">PRICING</a>
  <a class="nav-link" style="left:853px;top:70px">CONTACT US</a>
  <div class="pill chat-btn">
    <svg viewBox="0 0 24 24" fill="none" stroke="currentColor" stroke-width="1.8"><rect x="3" y="5" width="18" height="12" rx="5"/><path d="M8 11h8"/></svg>
    LIVE CHAT
  </div>
</header>

<section class="hero">
  <div class="hero-photo" role="img" aria-label="Photo of an adviser pointing a pen at a finance infographic on a desktop monitor"></div>
  <svg class="hero-overlay" viewBox="0 0 1200 802" preserveAspectRatio="none" aria-hidden="true">
    <polygon points="680,0 1200,0 1200,802 880,802" fill="#a8d8cb" fill-opacity=".55"/>
  </svg>
  <h1 class="hero-title">WE EMPOWER<br>BUSINESSES<br>LEDGRA CERTIFIED<br>RESULTS DRIVEN</h1>
  <div class="pill pill-outline hero-btn">GET STARTED
    <svg viewBox="0 0 24 24" fill="none" stroke="#a8d8cb" stroke-width="2"><circle cx="12" cy="12" r="9"/><circle cx="12" cy="12" r="3.5"/></svg>
  </div>
</section>

<section class="features">
  <div class="feature" style="left:87px">
    <svg width="60" height="66" viewBox="0 0 60 66" fill="none" stroke="#3d4a49" stroke-width="3"><rect x="10" y="4" width="40" height="58" rx="3"/><path d="M18 18h24M18 30h8M30 30h8M18 40h8M30 40h8M18 50h8M30 50h8"/></svg>
    <p>Tailored Financial<br>Solutions</p>
  </div>
  <div class="feature" style="left:436px">
    <svg width="110" height="66" viewBox="0 0 110 66" role="img" aria-label="Certification badge"><rect x="0" y="0" width="110" height="66" rx="10" fill="#3d4a49"/></svg>
    <p>Ledgra Advisor<br>Certified</p>
  </div>
  <div class="feature" style="left:784px">
    <svg width="96" height="84" viewBox="0 0 96 84" fill="none" stroke="#3d4a49" stroke-width="3"><path d="M6 44C20 22 76 22 90 44 76 66 20 66 6 44Z"/><circle cx="48" cy="44" r="16"/><path d="M48 4v10M22 12l6 8M74 12l-6 8M48 36v16M43 40h8M43 48h8"/></svg>
    <p>Enhanced<br>Financial Clarity</p>
  </div>
</section>

<section class="about">
  <div class="about-photo" role="img" aria-label="Photo of charts and reports on an office desk inside a circular frame"></div>
  <h2 class="section-title" style="left:618px;top:1357px">ABOUT US</h2>
  <div class="kicker" style="left:618px;top:1410px">WHO WE ARE <span class="dot"></span></div>
  <p class="about-copy" style="top:1452px">We pride ourselves on offering premium yet affordable accounting services to a wide range of organizations, with a focus on Crown Funded organisations supported by the Health Services Agency, Community Support Agency &amp; Learning Agency that deliver essential community-based services and programmes.</p>
  <p class="about-copy" style="top:1574px">This includes organisations operating under government contracts to provide services such as Mental Health Support, Residential Disability Care, Youth Development, Family and Social Services and other wellbeing initiatives. We also work with Charitable Trusts and Schools providing tailored support</p>
  <div class="pill pill-dark about-btn">KNOW MORE
    <svg viewBox="0 0 24 24" fill="none" stroke="#a8d8cb" stroke-width="2"><circle cx="12" cy="12" r="9"/><circle cx="12" cy="12" r="3.5"/></svg>
  </div>
</section>

<section class="banner">
  <div class="banner-photo" role="img" aria-label="Photo of two colleagues meeting at a table with a laptop and tablet"></div>
  <div class="banner-strip"></div>
  <div class="banner-ring"></div>
  <div class="banner-circle"></div>
  <p class="banner-text">LET VELLART BE THE CORNERSTONE OF YOUR FINANCIAL STABILITY AND GROWTH.</p>
  <div class="pill pill-dark banner-btn">LIVE CHAT
    <svg viewBox="0 0 24 24" fill="none" stroke="#a8d8cb" stroke-width="2"><circle cx="12" cy="12" r="9"/><circle cx="12" cy="12" r="3.5"/></svg>
  </div>
</section>

<section class="services">
  <h2 class="section-title" style="left:0;width:1200px;text-align:center;top:2518px">OUR SERVICES</h2>
  <div class="kicker centered" style="top:2575px"><span class="rule"></span><span class="dot"></span> WHAT WE DO <span class="dot"></span><span class="rule"></span></div>
  <p class="services-intro">We offer a comprehensive suite of accounting services to ensure your organization’s financial operations run smoothly and efficiently.</p>

  <div class="service" style="left:77px;top:2703px">
    <div class="service-icon"><svg width="48" height="48" viewBox="0 0 48 48" fill="none" stroke="#fff" stroke-width="2.5"><rect x="6" y="6" width="32" height="36" rx="2"/><path d="M12 30v6M19 24v12M26 18v18M12 14h20"/></svg></div>
    <h3>Monthly Reporting</h3>
    <p style="top:162px">Regular, detailed financial reports that give you a clear view of your financial position at all times.</p>
  </div>
  <div class="service highlight" style="left:436px;top:2703px">
    <div class="service-icon"><svg width="48" height="48" viewBox="0 0 48 48" fill="none" stroke="#fff" stroke-width="2.5"><rect x="8" y="4" width="26" height="36" rx="2"/><path d="M14 14h14M14 22h14M14 30h8"/><circle cx="34" cy="36" r="8"/></svg></div>
    <h3>Financial Performance &amp; Analysis</h3>
    <p style="top:182px">In-depth analysis to track profitability, identify trends, and support</p>
    <div class="read-more">READ MORE <svg width="22" height="22" viewBox="0 0 22 22" fill="none" stroke="#2b2f30" stroke-width="1.8"><circle cx="11" cy="11" r="9"/><path d="M7 11h8M12 8l3 3-3 3"/></svg></div>
  </div>
  <div class="service" style="left:800px;top:2703px">
    <div class="service-icon"><svg width="48" height="48" viewBox="0 0 48 48" fill="none" stroke="#fff" stroke-width="2.5"><rect x="6" y="6" width="36" height="28" rx="2"/><path d="M12 26l8-8 6 6 10-10M18 42h12"/></svg></div>
    <h3>Cash Flow Reporting</h3>
    <p style="top:158px">Accurate forecasting and monitoring of your cash flow to ensure liquidity and financial stability.</p>
  </div>

  <div class="service" style="left:77px;top:3042px">
    <div class="service-icon"><svg width="48" height="48" viewBox="0 0 48 48" fill="none" stroke="#fff" stroke-width="2.5"><rect x="6" y="4" width="30" height="38" rx="2"/><path d="M12 14h18M12 22h18M12 30h10"/><circle cx="36" cy="36" r="7"/></svg></div>
    <h3>GST, PAYE</h3>
    <p style="top:166px">Compliance with GST &amp; PAYE requirements, including accurate calculations, filings,</p>
  </div>
  <div class="service" style="left:436px;top:3042px">
    <div class="service-icon"><svg width="48" height="48" viewBox="0 0 48 48" fill="none" stroke="#fff" stroke-width="2.5"><rect x="6" y="6" width="24" height="32" rx="2"/><rect x="20" y="16" width="22" height="26" rx="2"/><path d="M12 14h12M26 26h10M26 33h10"/></svg></div>
    <h3>Payroll</h3>
    <p style="top:162px">In-depth analysis to track profitability, identify trends, and support strategic decisions.</p>
  </div>
  <div class="service" style="left:800px;top:3042px">
    <div class="service-icon"><svg width="48" height="48" viewBox="0 0 48 48" fill="none" stroke="#fff" stroke-width="2.5"><path d="M10 20c0-8 28-8 28 0v20H10Z"/><path d="M18 10l6-6 6 6M24 22v14M20 26h8M20 32h8"/></svg></div>
    <h3>Budgets &amp; Forecasts</h3>
    <p style="top:162px">Accurate forecasting and monitoring of your cash flow to ensure liquidity and financial stability.</p>
  </div>

  <div class="pill pill-dark services-btn">VIEW ALL SERVICES
    <svg viewBox="0 0 24 24" fill="none" stroke="#a8d8cb" stroke-width="2"><circle cx="12" cy="12" r="9"/><circle cx="12" cy="12" r="3.5"/></svg>
  </div>
</section>

<section class="reviews">
  <h2 class="section-title" style="left:0;width:1200px;text-align:center;top:3588px">CUSTOMER REVIEWS</h2>
  <div class="kicker centered" style="top:3640px"><span class="rule"></span><span class="dot"></span>TESTIMONIALS<span class="dot"></span><span class="rule"></span></div>

  <div class="arrow" style="left:10px;background:#e3e6e6"><svg width="14" height="14" viewBox="0 0 14 14" fill="none" stroke="#9aa09f" stroke-width="2"><path d="M9 2 4 7l5 5"/></svg></div>
  <div class="arrow" style="left:1146px;background:var(--mint)"><svg width="14" height="14" viewBox="0 0 14 14" fill="none" stroke="#fff" stroke-width="2"><path d="M5 2l5 5-5 5"/></svg></div>

  <div class="review" style="left:73px"><div class="quote">“</div><p>Lorem ipsum dolor sit amet, consectetur adipiscing elit. Sed vitae lobortis libero, at ultricies odio. Suspendisse vel sem in turpis tempus pretium.</p><div class="stars">★★★★★</div></div>
  <div class="review" style="left:430px"><div class="quote">“</div><p>Lorem ipsum dolor sit amet, consectetur adipiscing elit. Sed vitae lobortis libero, at ultricies odio. Suspendisse vel sem in turpis tempus pretium.</p><div class="stars">★★★★★</div></div>
  <div class="review" style="left:786px"><div class="quote">“</div><p>Lorem ipsum dolor sit amet, consectetur adipiscing elit. Sed vitae lobortis libero, at ultricies odio. Suspendisse vel sem in turpis tempus pretium.</p><div class="stars">★★★★★</div></div>

  <div class="reviewer" style="left:89px"><div class="avatar" role="img" aria-label="Reviewer portrait photo"></div><div><b>Jonah Smithers</b><span>Managing Director</span></div></div>
  <div class="reviewer" style="left:445px"><div class="avatar" role="img" aria-label="Reviewer portrait photo"></div><div><b>Stefan Kingsley</b><span>Managing Director</span></div></div>
  <div class="reviewer" style="left:802px"><div class="avatar" role="img" aria-label="Reviewer portrait photo"></div><div><b>Jonah Smithers</b><span>Managing Director</span></div></div>

  <div class="dots"><i class="on"></i><i></i><i></i><i></i></div>
</section>

<section class="contact">
  <div class="contact-photo" role="img" aria-label="Photo of a smiling office worker holding documents inside a circular frame"></div>
  <h2 class="section-title" style="left:612px;top:4168px">CONTACT US</h2>
  <div class="kicker" style="left:614px;top:4222px">GET IN TOUCH <span class="rule" style="width:150px;margin-left:8px"></span></div>
  <p class="contact-lead">Enter the fields of the following form to reach us</p>
  <div class="field" style="left:614px;top:4317px;width:220px;height:44px">First Name:</div>
  <div class="field" style="left:856px;top:4317px;width:221px;height:44px">Last Name:</div>
  <div class="field" style="left:614px;top:4381px;width:220px;height:45px">Phone:</div>
  <div class="field" style="left:856px;top:4381px;width:221px;height:45px">Email:</div>
  <div class="field" style="left:614px;top:4446px;width:463px;height:142px;padding-top:18px">Message:</div>
  <div class="pill pill-dark submit-btn">SUBMIT NOW
    <svg viewBox="0 0 24 24" fill="none" stroke="#a8d8cb" stroke-width="2"><circle cx="12" cy="12" r="9"/><circle cx="12" cy="12" r="3.5"/></svg>
  </div>
</section>

<footer class="site-footer">
  <div class="footer-head" style="left:281px;top:70px">QUICK LINKS</div>
  <ul class="quick-links">
    <li>Services</li><li>About Us</li><li>Pricing</li><li>Testimonials</li><li>Live Chat</li><li>Contact</li>
  </ul>
  <div class="brand footer-brand"><span class="brand-mark"></span><span class="brand-name">VELLART</span></div>
  <div class="social"><i></i><i></i><i></i></div>

  <div class="footer-head" style="left:760px;top:70px">CONTACT US</div>
  <div class="contact-item" style="top:142px"><span class="ico"><svg width="14" height="14" viewBox="0 0 14 14" fill="none" stroke="#fff" stroke-width="1.5"><path d="M3 1h2l1 3-1.5 1a8 8 0 0 0 4.5 4.5L10 8l3 1v2a2 2 0 0 1-2 2A10 10 0 0 1 1 3a2 2 0 0 1 2-2Z"/></svg></span><div>CALL US<br>021 555 0188</div></div>
  <div class="contact-item" style="top:190px"><span class="ico"><svg width="14" height="12" viewBox="0 0 14 12" fill="none" stroke="#fff" stroke-width="1.5"><rect x="1" y="1" width="12" height="10"/><path d="M1 1l6 5 6-5"/></svg></span><div>EMAIL US<br>contact@vellart.co.nz</div></div>
  <div class="contact-item" style="top:238px"><span class="ico"><svg width="12" height="14" viewBox="0 0 12 14" fill="none" stroke="#fff" stroke-width="1.5"><path d="M6 13S1 8 1 5a5 5 0 0 1 10 0c0 3-5 8-5 8Z"/><circle cx="6" cy="5" r="1.7"/></svg></span><div>Address line Dummy Here<br>Address line Here</div></div>

  <div class="footer-rule"></div>
  <p class="copyright">© 2025. All Rights Reserved.</p>
</footer>

</body>
</html>
```